2008年から発行を続けている当社唯一の社外報「星空MIDORI帖」の
1面に掲載するタイトル(見出し部分)のデザインを依頼いたします。
(添付参照:現在のタイトル)

〇星空MIDORI帖
・A4 8ページものの新聞
・知財関連のニュースやイベント、当社製品の紹介などを掲載
・年2度(6/11月)発行
・配布は印刷/データ(現在はデータの方が多い)

〇希望イメージ
・これまでの「真面目な」「由緒ある」といった印象だけではなく
「親しみやすさ」や「身近さ」「明るさ」「元気の良さ」「スタイリッシュさ」を伝えられる紙面にしたい
・読者は企業の知財部の方々なので子供っぽいデザインは避けたい
・企業カラーの緑色をベースにしたい

また、選ばせていただいたデザインをご提案いただいたデザイナー様には
続けてサブ見出し(1面以降のすべての紙面 上部中央に掲載する小さなもの)も
依頼させていただきたいと考えております。

以上、どうぞよろしくお願いいたします。
〇タイトル
・1面に掲載
・掲載サイズ:W188mm H76.6㎜
・入れていただきたい事項
①弊社所在地等の情報
第〇号
発行日(例:2022年3月23日)
発行 株式会社青葉書房社
https://www.aobashobo-sample.co.jp/
東京 千代田区外松原3-5-8 TEL:03-4927-6830
大阪 大阪市北区西桜台4-7-21 TEL:06-6718-2945
名古屋 刈谷市若草町5-14-3 TEL:0566-71-2049
②掲載記事のタイトルを記入できるスペース(W50mmH35.2mmほど)
希望イメージ
青系、緑系

弊社の希望する明るさ、爽やかさと知的財産を素敵に融合いただいたと感じました。
ご提案いただいた際の丁寧な文章も決め手の1つでした。

曖昧な依頼にも関わらず、たくさんのご提案をいただけ幸甚に存じます。
素敵なデザインばかりで今後の勉強にもさせていただきました。
1つしか当選にできず、心苦しい思いです。
この度は誠にありがとうございました。
皆様の益々のご活躍を祈念いたします。

```html
<!DOCTYPE html>
<html lang="ja">
<head>
<meta charset="utf-8">
<title>星空MIDORI帖 タイトルデザイン案</title>
<link rel="stylesheet" href="https://fonts.googleapis.com/css2?family=Noto+Sans+JP:wght@400;500;700;900&family=Oswald:wght@600;700&display=swap">
<style>
  :root{
    --green-deep:#16803a;
    --green:#36a83c;
    --green-soft:#7cc35a;
    --lime:#d9e87a;
    --lime-pale:#eef5c4;
    --ink:#1d3a22;
    --white:#ffffff;
    --paper:#ffffff;
  }
  *{box-sizing:border-box;margin:0;padding:0}
  html,body{width:848px;height:1200px;overflow:hidden;background:var(--paper)}
  body{font-family:"Noto Sans JP",sans-serif;color:var(--ink);position:relative}

  .sheet-label{position:absolute;left:34px;top:18px;font-size:13px;color:#555}

  .masthead{
    position:absolute;left:50px;width:748px;height:275px;
    border:5px solid var(--frame);border-radius:22px;background:var(--frame-fill);
    display:grid;grid-template-columns:205px 1fr;gap:10px;padding:10px;
  }
  .masthead--one{top:72px;--frame:var(--green);--frame-fill:var(--lime-pale);
    --toc-bg:var(--green);--toc-ink:var(--white);--toc-line:rgba(255,255,255,.6);--pill:var(--green-deep);
    --cell:var(--lime);--title:var(--green-deep);--info-bg:var(--green);--info-ink:var(--white);--issue:var(--lime)}
  .masthead--two{top:394px;--frame:var(--green);--frame-fill:var(--green-soft);
    --toc-bg:var(--lime-pale);--toc-ink:var(--ink);--toc-line:var(--green);--pill:var(--green);
    --cell:var(--lime);--title:var(--green-deep);--info-bg:var(--green-deep);--info-ink:var(--white);--issue:var(--lime)}
  .masthead--three{top:840px;--frame:var(--green-soft);--frame-fill:var(--lime-pale);
    --toc-bg:var(--white);--toc-ink:var(--ink);--toc-line:var(--green-soft);--pill:var(--green);
    --cell:var(--lime);--title:var(--green);--info-bg:var(--green-soft);--info-ink:var(--white);--issue:var(--white)}

  .toc{background:var(--toc-bg);color:var(--toc-ink);border-radius:14px;padding:12px 12px;position:relative}
  .masthead--three .toc{border:2px solid var(--green-soft)}
  .toc__label{display:inline-block;background:var(--pill);color:var(--white);font-weight:700;
    font-size:14px;padding:4px 16px;border-radius:14px;margin-bottom:12px;letter-spacing:.1em}
  .toc__list{list-style:none;font-size:10.5px;line-height:1.45}
  .toc__item{border-bottom:1px dashed var(--toc-line);padding:5px 0 4px}
  .toc__item::before{content:"● ";font-size:8px}
  .toc__page{display:block;text-align:right;font-weight:700}

  .title-grid{display:grid;grid-template-columns:1fr 190px;grid-template-rows:88px 76px 1fr;gap:6px}
  .title-cell{background:var(--cell);border-radius:10px;color:var(--title);font-weight:900;
    display:flex;align-items:center;justify-content:center;line-height:1}
  .title-cell--kanji{font-size:70px;letter-spacing:.1em}
  .title-cell--latin{grid-column:1 / 3;font-family:"Oswald",sans-serif;font-size:66px;letter-spacing:.28em;padding-left:.28em}
  .title-cell--last{font-size:70px}

  .issue{background:var(--info-bg);color:var(--info-ink);border-radius:10px;text-align:center;padding:6px 4px}
  .issue__reading{font-size:11px;letter-spacing:.25em}
  .issue__number{font-size:40px;font-weight:900;color:var(--issue);line-height:1.05}
  .issue__date{font-size:14px;font-weight:700;letter-spacing:.08em}

  .publisher{background:var(--info-bg);color:var(--info-ink);border-radius:10px;padding:6px 12px;font-size:10px;line-height:1.5}
  .publisher__name{font-size:12px;font-weight:700}
  .publisher__row{display:grid;grid-template-columns:44px 1fr 110px}
</style>
</head>
<body>
<p class="sheet-label">星空MIDORI帖 タイトルデザイン案</p>

<section class="masthead masthead--one">
  <div class="toc">
    <span class="toc__label">主な記事</span>
    <ul class="toc__list">
      <li class="toc__item">新製品・SDGsからみた日本企業の技術ポテンシャル<span class="toc__page">2面</span></li>
      <li class="toc__item">ブックステーション<span class="toc__page">2・3面</span></li>
      <li class="toc__item">最新案から物申す ― 連載第15回<span class="toc__page">3面</span></li>
      <li class="toc__item">お家時間を充実させるおすすめグッズ<span class="toc__page">4面</span></li>
    </ul>
  </div>
  <div class="title-grid">
    <div class="title-cell title-cell--kanji">星空</div>
    <div class="issue"><p class="issue__reading">ほしぞらみどりちょう</p><p class="issue__number">第26号</p><p class="issue__date">2021年11月15日</p></div>
    <div class="title-cell title-cell--latin">MIDORI</div>
    <div class="publisher">
      <p class="publisher__name">発行：株式会社青葉書房社</p>
      <p>https://www.aobashobo-sample.co.jp/</p>
      <p class="publisher__row"><span>東京</span><span>千代田区外松原3-5-8</span><span>TEL:03-4927-6830</span></p>
      <p class="publisher__row"><span>大阪</span><span>大阪市北区西桜台4-7-21</span><span>TEL:06-6718-2945</span></p>
      <p class="publisher__row"><span>名古屋</span><span>刈谷市若草町5-14-3</span><span>TEL:0566-71-2049</span></p>
    </div>
    <div class="title-cell title-cell--last">帖</div>
  </div>
</section>

<section class="masthead masthead--two">
  <div class="toc">
    <span class="toc__label">主な記事</span>
    <ul class="toc__list">
      <li class="toc__item">新製品・SDGsからみた日本企業の技術ポテンシャル<span class="toc__page">2面</span></li>
      <li class="toc__item">ブックステーション<span class="toc__page">2・3面</span></li>
      <li class="toc__item">最新案から物申す ― 連載第15回<span class="toc__page">3面</span></li>
      <li class="toc__item">お家時間を充実させるおすすめグッズ<span class="toc__page">4面</span></li>
    </ul>
  </div>
  <div class="title-grid">
    <div class="title-cell title-cell--kanji">星空</div>
    <div class="issue"><p class="issue__reading">ほしぞらみどりちょう</p><p class="issue__number">第26号</p><p class="issue__date">2021年11月15日</p></div>
    <div class="title-cell title-cell--latin">MIDORI</div>
    <div class="publisher">
      <p class="publisher__name">発行：株式会社青葉書房社</p>
      <p>https://www.aobashobo-sample.co.jp/</p>
      <p class="publisher__row"><span>東京</span><span>千代田区外松原3-5-8</span><span>TEL:03-4927-6830</span></p>
      <p class="publisher__row"><span>大阪</span><span>大阪市北区西桜台4-7-21</span><span>TEL:06-6718-2945</span></p>
      <p class="publisher__row"><span>名古屋</span><span>刈谷市若草町5-14-3</span><span>TEL:0566-71-2049</span></p>
    </div>
    <div class="title-cell title-cell--last">帖</div>
  </div>
</section>

<section class="masthead masthead--three">
  <div class="toc">
    <span class="toc__label">主な記事</span>
    <ul class="toc__list">
      <li class="toc__item">新製品・SDGsからみた日本企業の技術ポテンシャル<span class="toc__page">2面</span></li>
      <li class="toc__item">ブックステーション<span class="toc__page">2・3面</span></li>
      <li class="toc__item">最新案から物申す ― 連載第15回<span class="toc__page">3面</span></li>
      <li class="toc__item">お家時間を充実させるおすすめグッズ<span class="toc__page">4面</span></li>
    </ul>
  </div>
  <div class="title-grid">
    <div class="title-cell title-cell--kanji">星空</div>
    <div class="issue"><p class="issue__reading">ほしぞらみどりちょう</p><p class="issue__number">第26号</p><p class="issue__date">2021年11月15日</p></div>
    <div class="title-cell title-cell--latin">MIDORI</div>
    <div class="publisher">
      <p class="publisher__name">発行：株式会社青葉書房社</p>
      <p>https://www.aobashobo-sample.co.jp/</p>
      <p class="publisher__row"><span>東京</span><span>千代田区外松原3-5-8</span><span>TEL:03-4927-6830</span></p>
      <p class="publisher__row"><span>大阪</span><span>大阪市北区西桜台4-7-21</span><span>TEL:06-6718-2945</span></p>
      <p class="publisher__row"><span>名古屋</span><span>刈谷市若草町5-14-3</span><span>TEL:0566-71-2049</span></p>
    </div>
    <div class="title-cell title-cell--last">帖</div>
  </div>
</section>
</body>
</html>
```